I am a highly experienced private practice psychotherapist serving high end clientele in the Wall Street area of New York City. I need electronic letterhead (that can also be printed) to use for bills, receipts, and correspondences.

My clients are very high end and are used to elegance and wealth. The letterhead should contain the following information: Marissa K. Tolland, LCSW 57 Pinegate Avenue, Suite 2716 New York, NY 10392 Phone : (917) 555-3179 email: therapy@marissatollandlcsw.example website: www.marissatollandlcsw.example

Thank you for your designs. Please be advised that the letterhead will be used for bills/invoices; professional letters to other mental health professionals and doctors, as well as to attorneys. It needs to be highly professional in the same way that a law firm has professional and elegant letterhead, raher than whimsical or with spa designers. My letters end up as official documents.

```html
<!DOCTYPE html>
<html lang="en">
<head>
<meta charset="utf-8">
<title>Marissa K. Tolland, LCSW — Letterhead</title>
<link href="https://fonts.googleapis.com/css2?family=Arimo:wght@400;700&family=Tinos:ital,wght@0,400;1,700&display=swap" rel="stylesheet">
<style>
  :root {
    --ink: #111111;
    --paper: #ffffff;
    --teal: #7dddd0;
    --rule: #555555;
    --stone-dark: #4f4f55;
    --stone-green: #8fcf9c;
  }
  html, body {
    margin: 0;
    padding: 0;
    width: 927px;
    height: 1200px;
    overflow: hidden;
    background: var(--paper);
  }
  .letterhead {
    position: relative;
    width: 927px;
    height: 1200px;
    background: var(--paper);
    font-family: "Arimo", Arial, sans-serif;
    color: var(--ink);
  }
  .band {
    position: absolute;
    left: 0;
    width: 927px;
  }
  .band--top { top: 0; height: 90px; }
  .band--bottom { bottom: 0; height: 80px; }
  .brand-mark {
    position: absolute;
    left: 84px;
    top: 100px;
    width: 104px;
    display: flex;
    align-items: center;
    gap: 7px;
    font-weight: 700;
    font-size: 14px;
  }
  .brand-mark__square {
    width: 12px;
    height: 12px;
    background: var(--ink);
    flex: none;
  }
  .identity {
    position: absolute;
    left: 200px;
    top: 84px;
    line-height: 1.15;
  }
  .identity__name {
    margin: 0;
    font-size: 17px;
    font-weight: 700;
    font-variant: small-caps;
    letter-spacing: 0.3px;
  }
  .identity__practice {
    margin: 1px 0 0;
    font-family: "Tinos", "Times New Roman", serif;
    font-style: italic;
    font-weight: 700;
    font-size: 15.5px;
  }
  .identity__focus {
    margin: 0;
    font-family: "Tinos", "Times New Roman", serif;
    font-size: 15.5px;
  }
  .identity__address {
    margin: 12px 0 0;
    font-style: normal;
    font-size: 15px;
    line-height: 1.2;
  }
  .contact {
    position: absolute;
    left: 542px;
    top: 104px;
    margin: 0;
    padding: 0;
    list-style: none;
    font-size: 14.5px;
  }
  .contact__item {
    display: flex;
    align-items: center;
    gap: 8px;
    height: 23px;
  }
  .contact__icon { width: 13px; height: 13px; flex: none; }
  .header-rule {
    position: absolute;
    left: 38px;
    top: 204px;
    width: 820px;
    height: 1px;
    background: var(--rule);
  }
  .stones-photo {
    position: absolute;
    left: 33px;
    top: 893px;
    width: 124px;
    height: 240px;
    background: linear-gradient(180deg, var(--stone-dark) 0%, #7b9f84 45%, var(--stone-green) 100%);
    border-radius: 40px 40px 6px 6px;
  }
</style>
</head>
<body>
<div class="letterhead">
  <svg class="band band--top" viewBox="0 0 927 90" preserveAspectRatio="none" aria-hidden="true">
    <path d="M0,0 H927 V8 C860,50 760,80 640,80 C520,80 420,66 300,60 C180,54 80,58 0,62 Z" fill="var(--teal)"/>
    <path d="M0,0 H927 V4 C870,34 780,62 650,62 C530,62 420,50 300,46 C180,42 80,46 0,50 Z" fill="var(--ink)"/>
  </svg>

  <div class="brand-mark"><span class="brand-mark__square"></span>Tolland</div>

  <div class="identity">
    <h1 class="identity__name">Marissa K. Tolland, LCSW</h1>
    <p class="identity__practice">Psychotherapy</p>
    <p class="identity__focus">Individual, Family, Relationship</p>
    <address class="identity__address">57 Pinegate Avenue, Suite 2716<br>New York, NY 10392</address>
  </div>

  <ul class="contact">
    <li class="contact__item">
      <svg class="contact__icon" viewBox="0 0 13 13" aria-hidden="true"><circle cx="6.5" cy="6.5" r="6.5" fill="var(--ink)"/><path d="M4,3.2 L5.4,3 L6,5 L5.2,5.8 C5.7,7 6.2,7.5 7.3,8 L8.1,7.2 L10,7.8 L9.8,9.2 C7,9.6 3.6,6.4 4,3.2 Z" fill="var(--paper)"/></svg>
      Phone : (917) 555-3179
    </li>
    <li class="contact__item">
      <svg class="contact__icon" viewBox="0 0 13 13" aria-hidden="true"><circle cx="6.5" cy="6.5" r="6.5" fill="var(--ink)"/><rect x="3.2" y="4.2" width="6.6" height="4.6" fill="none" stroke="var(--paper)" stroke-width="1"/><path d="M3.2,4.2 L6.5,6.8 L9.8,4.2" fill="none" stroke="var(--paper)" stroke-width="1"/></svg>
      email: therapy@marissatollandlcsw.example
    </li>
    <li class="contact__item">
      <svg class="contact__icon" viewBox="0 0 13 13" aria-hidden="true"><circle cx="6.5" cy="6.5" r="6.5" fill="var(--ink)"/><circle cx="6.5" cy="6.5" r="3.6" fill="none" stroke="var(--paper)" stroke-width="0.9"/><ellipse cx="6.5" cy="6.5" rx="1.5" ry="3.6" fill="none" stroke="var(--paper)" stroke-width="0.9"/><line x1="2.9" y1="6.5" x2="10.1" y2="6.5" stroke="var(--paper)" stroke-width="0.9"/></svg>
      website: www.marissatollandlcsw.example
    </li>
  </ul>

  <div class="header-rule"></div>

  <div class="stones-photo" role="img" aria-label="Photograph of a stack of smooth grey and green stones"></div>

  <svg class="band band--bottom" viewBox="0 0 927 80" preserveAspectRatio="none" aria-hidden="true">
    <path d="M33,14 L927,6 V80 H33 Z" fill="var(--teal)"/>
    <path d="M33,24 L927,17 V80 H33 Z" fill="var(--ink)"/>
  </svg>
</div>
</body>
</html>
```